National Sports Business needs a Flyer Design

We need a flyer, which gives an interested person an overview of our "product range". We offer perfomance testing (Leistungsdiagnostik), Personal-Training (the same in German), Strength Training (Athletiktraining), planning individual trainings (Trainingsplanung), company fitness (Firmenbetreuung), swim training (Schwimmtraining). There should also be our contact datas on it:
KVL - Kinetic Vantage Lab
Moosweg 18
2587 Haselbrunn
+43 664 31 82 905
office@kineticvantagelab.at
www.kineticvantagelab.at

If you need fotos for the flyer, you will find a lot of my facebookpage https://www.facebook.com/kineticvantagelab/?ref=bookmarks

NEW FOTOS ON THE FACEBOOKSITE!!!

Target Market(s)

companies, beginners, advanced, runners, triathletes,

Industry/Entity Type

Business

Requirements
Must have
• The Text should be in german words (in brackets).

```html
<!DOCTYPE html>
<html lang="de">
<head>
<meta charset="utf-8">
<title>KVL - Kinetic Vantage Lab Flyer</title>
<link href="https://fonts.googleapis.com/css2?family=Bebas+Neue&family=Open+Sans:wght@400&display=swap" rel="stylesheet">
<style>
  :root {
    --brand-blue: #0e4592;
    --service-blue: #1f4e96;
    --paper: #ffffff;
    --ink: #333333;
    --photo-dark: #3a3f4a;
    --photo-light: #b9b6b2;
  }
  * { margin: 0; padding: 0; box-sizing: border-box; }
  html, body { width: 924px; height: 1200px; overflow: hidden; background: var(--paper); }
  .flyer { position: relative; width: 924px; height: 1200px; background: var(--paper); overflow: hidden; }
  .hero { position: absolute; left: 0; top: 0; width: 924px; height: 1200px; }
  .brand-mark {
    position: absolute; left: 198px; top: 104px; transform: translate(-50%, -50%);
    display: flex; align-items: center; gap: 12px;
    font-family: "Bebas Neue", sans-serif; font-size: 72px; line-height: 1;
    color: var(--brand-blue);
  }
  .brand-mark .square { width: 20px; height: 20px; background: var(--brand-blue); }
  .services { position: absolute; left: 0; width: 924px; font-family: "Bebas Neue", sans-serif; font-size: 29px; color: var(--service-blue); }
  .service, .dot { position: absolute; top: 0; transform: translate(-50%, -50%); white-space: nowrap; }
  .dot { width: 9px; height: 9px; border-radius: 50%; background: var(--service-blue); }
  .row-one { top: 925px; }
  .row-two { top: 1005px; }
  .footer-logo {
    position: absolute; left: 138px; top: 1111px; transform: translate(-50%, -50%);
    font-family: "Bebas Neue", sans-serif; font-size: 46px; line-height: 1; color: var(--brand-blue);
  }
  .divider { position: absolute; top: 1074px; width: 2px; height: 76px; background: var(--brand-blue); }
  .contact {
    position: absolute; top: 1111px; transform: translate(-50%, -50%);
    font-family: "Open Sans", sans-serif; font-size: 15.5px; line-height: 1.35;
    color: var(--ink); text-align: center; white-space: nowrap;
  }
</style>
</head>
<body>
<main class="flyer">
  <svg class="hero" viewBox="0 0 955 1352" preserveAspectRatio="none" width="924" height="1200">
    <defs>
      <linearGradient id="mainPhotoTone" x1="0" y1="0" x2="1" y2="1">
        <stop offset="0" stop-color="#c9c6c1"/>
        <stop offset="0.55" stop-color="#8a7c72"/>
        <stop offset="1" stop-color="#2c2e36"/>
      </linearGradient>
      <linearGradient id="sidePhotoTone" x1="0" y1="0" x2="1" y2="1">
        <stop offset="0" stop-color="#6f6b68"/>
        <stop offset="1" stop-color="#b4b1ae"/>
      </linearGradient>
    </defs>
    <polygon points="0,285 418,808 0,1047" fill="url(#sidePhotoTone)" role="img" aria-label="Foto: Trainer sichert eine Frau beim Bankdrücken mit der Langhantel"/>
    <polygon points="137,330 650,0 955,0 955,720 555,977" fill="url(#mainPhotoTone)" role="img" aria-label="Foto: Athlet drückt Kurzhanteln über Kopf, Trainer korrigiert die Armhaltung"/>
    <polygon points="0,124 555,977 0,285" fill="var(--brand-blue)"/>
    <polygon points="137,330 558,0 650,0" fill="var(--brand-blue)"/>
    <polygon points="555,977 955,720 955,780" fill="var(--brand-blue)"/>
  </svg>

  <div class="brand-mark"><span class="square"></span><span class="name">KVL</span></div>

  <section class="services row-one">
    <span class="service" style="left:233px">Athletiktraining</span>
    <span class="dot" style="left:351px"></span>
    <span class="service" style="left:470px">Trainingsplanung</span>
    <span class="dot" style="left:590px"></span>
    <span class="service" style="left:706px">Schwimmtraining</span>
  </section>
  <section class="services row-two">
    <span class="service" style="left:196px">Leistungsdiagnostik</span>
    <span class="dot" style="left:339px"></span>
    <span class="service" style="left:471px">Personal-Training</span>
    <span class="dot" style="left:610px"></span>
    <span class="service" style="left:736px">Firmenbetreuung</span>
  </section>

  <footer>
    <div class="footer-logo">KVL</div>
    <span class="divider" style="left:244px"></span>
    <p class="contact" style="left:328px">KVL - Kinetic<br>Vantage Lab</p>
    <span class="divider" style="left:424px"></span>
    <p class="contact" style="left:516px">Moosweg 18<br>2587 Haselbrunn<br>+43 664 31 82 905</p>
    <span class="divider" style="left:611px"></span>
    <p class="contact" style="left:750px">office@kineticvantagelab.at<br>www.kineticvantagelab.at</p>
  </footer>
</main>
</body>
</html>
```